wedding photography website for top wedding photographer

I have a website right now that is barely working. I want the photos to maybe all the photos lined up horizontally and you scroll to see the images. I have an orange logo and want it to be dark grey. I also need a page for publications (I have those as scans) and a link to an About page.

Target Market(s)

wedding planners and bride

Industry/Entity Type

Wedding Photography

Coding

Coded - Design and coding required

Number of Pages Required

5+ page

Font styles to use
Serif
Sans Serif

Colors
ffffff
474747

Requirements
Must have
• easy to navigate, always want the instagram and contact info readily available, should be clean and modern and let the photos stand out. it's wedding photos but i don't want it to feel girly or prissy.
Nice to have
• possibly could be one big photo on the home page, then click it to go into all the other photos. want page options on the home page and every page
Should not have
• nothing fussy or quaint, want this to be the "Copper Ladle" restaurant of wedding photography

```html
<!DOCTYPE html>
<html lang="en">
<head>
<meta charset="utf-8">
<title>Lena Hart Photography – Journal Entry</title>
<link href="https://fonts.googleapis.com/css2?family=Oswald:wght@300;400&family=Alegreya:wght@400;500;700&display=swap" rel="stylesheet">
<style>
  :root {
    --accent: #e8601c;
    --page: #474747;
    --band: #3a3a3a;
    --nav: #2e2e2e;
    --card: #393939;
    --field: #353535;
    --text: #f2f2f2;
    --muted: #bdbdbd;
    --white: #ffffff;
  }
  * { margin: 0; padding: 0; box-sizing: border-box; }
  html, body { width: 1200px; height: 2951px; overflow: hidden; }
  body {
    position: relative;
    background: var(--page);
    color: var(--text);
    font-family: "Alegreya", serif;
  }
  .abs { position: absolute; }

  /* navigation */
  .site-nav { left: 0; top: 0; width: 1200px; height: 50px; background: var(--nav); border-bottom: 1px solid #555; }
  .brand { left: 89px; top: 12px; font-family: "Alegreya", serif; font-size: 19px; color: var(--accent); font-weight: 500; }
  .menu { right: 89px; top: 16px; display: flex; gap: 17px; list-style: none; font-size: 13px; letter-spacing: .4px; color: var(--muted); text-transform: uppercase; }

  /* hero */
  .hero-band { left: 0; top: 50px; width: 1200px; height: 388px; background: var(--band); }
  .hero-photo {
    left: 89px; top: 93px; width: 1022px; height: 573px;
    border: 7px solid var(--white);
    background:
      radial-gradient(ellipse at 62% 45%, #c9c1b8 0%, #b58c76 18%, transparent 40%),
      radial-gradient(ellipse at 78% 60%, #5e4aa8 0%, transparent 30%),
      linear-gradient(135deg, #e07a4a 0%, #d05a32 35%, #b84a2c 60%, #c86a3c 80%, #8a3a22 100%);
  }

  /* post header */
  .post-title { left: 89px; top: 724px; font-family: "Oswald", sans-serif; font-weight: 300; font-size: 37px; line-height: 49px; color: var(--accent); text-transform: uppercase; letter-spacing: .3px; }
  .post-meta { right: 89px; top: 729px; display: flex; gap: 22px; font-size: 11px; color: var(--muted); align-items: center; }
  .post-meta span { display: flex; align-items: center; gap: 5px; }
  .meta-rule { left: 787px; top: 765px; width: 324px; height: 1px; background: #6a6a6a; }
  .share { right: 89px; top: 777px; display: flex; align-items: center; gap: 8px; font-size: 11px; color: var(--muted); }
  .share-dot { width: 24px; height: 24px; border: 1px solid var(--accent); border-radius: 50%; }

  .post-body { left: 89px; top: 884px; width: 1022px; font-size: 13px; line-height: 20.5px; text-align: justify; color: var(--text); }
  .post-body p + p { margin-top: 21px; }

  /* tags */
  .tags-band { left: 0; top: 1119px; width: 1200px; height: 302px; background: var(--band); }
  .section-head { display: flex; align-items: center; gap: 8px; font-family: "Oswald", sans-serif; font-weight: 300; font-size: 24px; color: var(--accent); text-transform: uppercase; }
  .tag { height: 48px; border: 2px solid var(--accent); display: flex; align-items: center; justify-content: center; font-size: 13px; color: var(--text); }

  /* comment form */
  .form-intro { left: 89px; top: 1533px; width: 420px; font-size: 13px; line-height: 22px; }
  .field-label { font-size: 17px; text-transform: uppercase; letter-spacing: .3px; }
  .field { background: var(--field); color: var(--accent); font-size: 12px; padding: 12px 12px; }
  .send { left: 964px; top: 1908px; width: 147px; height: 49px; background: var(--accent); color: var(--white); font-family: "Oswald", sans-serif; font-size: 17px; display: flex; align-items: center; justify-content: center; }
  .divider { left: 89px; top: 2002px; width: 1022px; height: 1px; background: #6a6a6a; }

  /* comments */
  .comment { background: var(--card); border-left: 3px solid var(--accent); }
  .avatar { border: 4px solid var(--accent); }
  .commenter { font-size: 17px; font-weight: 700; color: var(--accent); }
  .comment-date { font-size: 11px; color: var(--accent); }
  .dots { height: 0; border-top: 1px dashed #888; }
  .comment-text { font-size: 12.5px; line-height: 18.5px; text-align: justify; }
  .reply { width: 148px; height: 47px; border: 2px solid var(--accent); color: var(--accent); font-family: "Oswald", sans-serif; font-size: 15px; display: flex; align-items: center; justify-content: center; }

  /* pagination */
  .pager { top: 2772px; font-size: 12px; color: var(--muted); }

  /* footer */
  .footer-rule { top: 2865px; height: 2px; background: var(--accent); }
  .copyright { left: 0; top: 2855px; width: 1200px; text-align: center; font-size: 12px; color: var(--accent); }
</style>
</head>
<body>

<header class="abs site-nav">
  <div class="abs brand">Lena Hart Photography</div>
  <ul class="abs menu">
    <li>Home</li><li>Gallery</li><li>Publication</li><li>Link</li><li>Contact</li><li>About</li>
  </ul>
</header>

<div class="abs hero-band"></div>
<div class="abs hero-photo" role="img" aria-label="Wedding photograph of a bride and groom embracing in an autumn forest under a flower arch"></div>

<h1 class="abs post-title">Lorem ipsum dolores<br>consecture adiciting elit tempor</h1>

<div class="abs post-meta">
  <span><svg width="14" height="10" viewBox="0 0 14 10"><path d="M1 5C3 1 11 1 13 5C11 9 3 9 1 5Z" fill="none" stroke="#bdbdbd" stroke-width="1.3"/><circle cx="7" cy="5" r="2" fill="#bdbdbd"/></svg>253</span>
  <span><svg width="12" height="11" viewBox="0 0 12 11"><path d="M1 1H11V7H5L2 10V7H1Z" fill="#bdbdbd"/></svg>102</span>
  <span><svg width="11" height="11" viewBox="0 0 11 11"><circle cx="5.5" cy="5.5" r="4.8" fill="none" stroke="#bdbdbd" stroke-width="1.2"/><path d="M5.5 2.5V5.5H8" fill="none" stroke="#bdbdbd" stroke-width="1.2"/></svg>Jun 05 2018</span>
</div>
<div class="abs meta-rule"></div>
<div class="abs share">
  <svg width="12" height="10" viewBox="0 0 12 10"><path d="M7 1L11 5L7 9V6.5C4 6.5 2 7.5 1 9C1.5 5.5 3.5 3.8 7 3.5Z" fill="#bdbdbd"/></svg>
  Share to :
  <span class="share-dot"></span><span class="share-dot"></span><span class="share-dot"></span><span class="share-dot"></span>
</div>

<div class="abs post-body">
  <p>Constantia lorem ipsum dolor sit amet, consectetur adipiscing elit. Nulla congue orci id bibendum tempor. Donec facilisis, ipsum et mollis aliquam, nisi eros sollicitudin velit, eu faucibus arcu neque in quam. Quisque auctor ullamcorper blandit. Ut vitae ultricies lorem. Proin facilisis tempor velit nec vehicula. Curabitur scelerisque fringilla ultrices. Integer non accumsan tellus, ut congue lorem. Aliquam velit purus, varius et nulla id, pellentesque varius nulla. Phasellus commodo semper arcu, vitae scelerisque leo sodales id. Nullam ut placerat quam. Etiam nec elementum felis. Morbi a nisl accumsan, sagittis quam in, faucibus orci.</p>
  <p>Lorem ipsum dolor sit amet, consectetur adipiscing elit. Nulla congue orci id bibendum tempor. Donec facilisis, ipsum et mollis aliquam, nisi eros sollicitudin velit, eu faucibus arcu neque in quam. Quisque auctor ullamcorper blandit. Ut vitae ultricies lorem. Proin facilisis tempor velit nec vehicula. Curabitur scelerisque fringilla ultrices. Integer non accumsan tellus, ut congue lorem. Aliquam velit purus, varius et nulla id, pellentesque varius nulla. Phasellus commodo semper arcu, vitae scelerisque leo sodales id. Nullam ut placerat quam. Etiam nec elementum felis. Morbi a nisl accumsan, sagittis quam in, faucibus orci.</p>
</div>

<section>
  <div class="abs tags-band"></div>
  <h2 class="abs section-head" style="left:89px;top:1160px;">
    <svg width="26" height="24" viewBox="0 0 26 24"><path d="M1 2V10L12 21L21 12L10 1H2Z" fill="#e8601c"/><circle cx="6" cy="6" r="2" fill="#3a3a3a"/><path d="M14 1L24 11L15 21" fill="none" stroke="#e8601c" stroke-width="2"/></svg>
    Tags :
  </h2>
  <div class="abs tag" style="left:89px;top:1234px;width:147px;">Lorem Ipsum</div>
  <div class="abs tag" style="left:263px;top:1234px;width:94px;">Lorem</div>
  <div class="abs tag" style="left:384px;top:1234px;width:147px;">Lorem Ipsum</div>
  <div class="abs tag" style="left:558px;top:1234px;width:94px;">Lorem</div>
  <div class="abs tag" style="left:679px;top:1234px;width:93px;">Lorem</div>
  <div class="abs tag" style="left:802px;top:1234px;width:98px;">Lorem</div>
  <div class="abs tag" style="left:927px;top:1234px;width:148px;">Lorem Ipsum</div>
  <div class="abs tag" style="left:89px;top:1308px;width:93px;">Lorem</div>
  <div class="abs tag" style="left:209px;top:1308px;width:148px;">Lorem Ipsum</div>
  <div class="abs tag" style="left:384px;top:1308px;width:93px;">Lorem</div>
  <div class="abs tag" style="left:504px;top:1308px;width:94px;">Lorem</div>
  <div class="abs tag" style="left:632px;top:1308px;width:93px;">Lorem</div>
</section>

<section>
  <h2 class="abs section-head" style="left:89px;top:1466px;">
    <svg width="24" height="20" viewBox="0 0 24 20"><path d="M12 1C5.5 1 1 4.8 1 9C1 11.5 2.6 13.6 5 15L4 19L9 16.5C10 16.8 11 17 12 17C18.5 17 23 13.2 23 9C23 4.8 18.5 1 12 1Z" fill="#e8601c"/></svg>
    Comments
  </h2>
  <p class="abs form-intro">Type your comment to appreciate this photo. Your e-mail address will not be published. Required fields are marked *.</p>

  <label class="abs field-label" style="left:89px;top:1610px;">Name *</label>
  <div class="abs field" style="left:89px;top:1643px;width:410px;height:44px;">Type your name here</div>
  <label class="abs field-label" style="left:89px;top:1708px;">E-mail *</label>
  <div class="abs field" style="left:89px;top:1743px;width:410px;height:45px;">Type your e-mail here</div>
  <label class="abs field-label" style="left:89px;top:1809px;">Website</label>
  <div class="abs field" style="left:89px;top:1844px;width:410px;height:45px;">Type your website here</div>
  <label class="abs field-label" style="left:526px;top:1610px;">Commentar box *</label>
  <div class="abs field" style="left:526px;top:1643px;width:585px;height:246px;">Type your comments here</div>
  <div class="abs send">SEND</div>
</section>

<div class="abs divider"></div>

<article>
  <div class="abs comment" style="left:202px;top:2046px;width:909px;height:322px;"></div>
  <div class="abs avatar" role="img" aria-label="Portrait photo of the commenter" style="left:89px;top:2095px;width:147px;height:145px;background:linear-gradient(160deg,#6f86a8,#8a7468 55%,#2f3442);"></div>
  <div class="abs commenter" style="left:263px;top:2092px;">Martin Roswell Says:</div>
  <div class="abs comment-date" style="left:263px;top:2116px;">September 30, 2018 at 10:30 am</div>
  <div class="abs dots" style="left:263px;top:2157px;width:829px;"></div>
  <p class="abs comment-text" style="left:263px;top:2178px;width:829px;">Constantia lorem ipsum dolor sit amet, consectetur adipiscing elit. Nulla congue orci id bibendum tempor. Donec facilisis, ipsum et mollis aliquam, nisi eros sollicitudin velit, eu faucibus arcu neque in quam. Quisque auctor ullamcorper blandit. Ut vitae ultricies lorem. Proin facilisis tempor velit nec vehicula. Curabitur scelerisque fringilla ultrices. Integer non accumsan tellus, ut congue lorem. Aliquam velit purus, varius et nulla id, pellentesque varius nulla. Phasellus commodo semper arcu, vitae scelerisque leo sodales id. Nullam ut placerat quam. Etiam nec elementum felis.</p>
  <div class="abs reply" style="left:944px;top:2277px;">REPLY</div>
</article>

<article>
  <div class="abs comment" style="left:312px;top:2380px;width:799px;height:322px;"></div>
  <div class="abs avatar" role="img" aria-label="Portrait photo of the commenter" style="left:202px;top:2427px;width:142px;height:143px;background:linear-gradient(170deg,#9b8a70,#c9b9a4 50%,#e8e6e2);"></div>
  <div class="abs commenter" style="left:374px;top:2421px;">Clara Venn Says:</div>
  <div class="abs comment-date" style="left:374px;top:2446px;">September 30, 2018 at 10:30 am</div>
  <div class="abs dots" style="left:374px;top:2489px;width:718px;"></div>
  <p class="abs comment-text" style="left:374px;top:2508px;width:718px;">Constantia lorem ipsum dolor sit amet, consectetur adipiscing elit. Nulla congue orci id bibendum tempor. Donec facilisis, ipsum et mollis aliquam, nisi eros sollicitudin velit, eu faucibus arcu neque in quam. Quisque auctor ullamcorper blandit. Ut vitae ultricies lorem. Proin facilisis tempor velit nec vehicula. Curabitur scelerisque fringilla ultrices. Integer non accumsan tellus, ut congue lorem. Aliquam velit purus, varius et nulla id, pellentesque varius nulla. Phasellus commodo semper arcu, vitae scelerisque leo.</p>
  <div class="abs reply" style="left:944px;top:2611px;">REPLY</div>
</article>

<nav aria-label="Pagination">
  <svg class="abs" style="left:263px;top:2776px;" width="20" height="16" viewBox="0 0 20 16"><path d="M19 8H3M9 2L2 8L9 14" fill="none" stroke="#fff" stroke-width="2.5"/></svg>
  <span class="abs pager" style="left:361px;">1</span>
  <span class="abs pager" style="left:417px;color:#fff;">2</span>
  <span class="abs pager" style="left:474px;">3</span>
  <span class="abs pager" style="left:533px;">4</span>
  <span class="abs pager" style="left:590px;">5</span>
  <span class="abs pager" style="left:651px;">6</span>
  <span class="abs pager" style="left:710px;">7</span>
  <span class="abs pager" style="left:769px;">8</span>
  <span class="abs pager" style="left:828px;">9</span>
  <svg class="abs" style="left:915px;top:2776px;" width="20" height="16" viewBox="0 0 20 16"><path d="M1 8H17M11 2L18 8L11 14" fill="none" stroke="#fff" stroke-width="2.5"/></svg>
</nav>

<footer>
  <div class="abs footer-rule" style="left:89px;width:378px;"></div>
  <div class="abs footer-rule" style="left:738px;width:373px;"></div>
  <p class="abs copyright">© copyright 2018 www.lenahartphoto.com</p>
</footer>

</body>
</html>
```